New Packaging Design Project for Matcha Green Tea

**I've added an image called 'Sizing example', this is to show you the size of the label compared to the pack. Currently we are using full size labels for the pack and they are too difficult to apply.
Hi. I need a new label creating for a 100g pack of stunning organic premium grade Matcha tea.
The label needs to be 69mm by 88.9mm on the finished product and will be placed on a foil pack which is somewhat larger than the label.
Needs to include the text:
"Matcha Green Tea"
"Organic Japanese Premium Grade"
"Perfect for drinking, blending and baking"
"100g"
Attaching our logo and the KPV certification which both need to be on the label.
You can see our other products at www.leafhollowco.co.uk
You key with this product is that we need it to stand out on Bazolia. There are many, many other Matcha products in foil packs, so this needs to be a bold and fresh design. My suggestion is to test the design by editing it into a screenshot of the Bazolia search page for matcha tea to see if it stands out.
Target Market(s)
Affluent health conscious individuals. Those with busy life, such as executives or parents,. Those with an active life, such as triathletes, yoga, cyclists. Those with a aspirational life, i.e. they want to have quality in their life and they aspire to have the latest trends.
Requirements
Must have
- Stand out design. Clear, clean, crisp.
- Our green colour is #63A802 / 99 / 168 / 2. C41, M0, Y99, K34
- We also sometimes use #144400- R: 20 G: 68 B: 0
Nice to have
- Could either show how the product is used - i.e. lifestyle or just show the quality of the product.
- Could show the product in a ceremonial style bowl, a matcha latte or being blended or used for baking. Could even show all of these, so long as it doesn't look 'busy'.
Should not have
- Clutter, too many things going on.

```html
<!DOCTYPE html>
<html lang="en">
<head>
<meta charset="utf-8">
<title>Leaf Hollow Matcha Green Tea Label</title>
<link href="https://fonts.googleapis.com/css2?family=Oswald:wght@500;600&family=Quicksand:wght@400&display=swap" rel="stylesheet">
<style>
  :root {
    --backdrop: #04633f;
    --label: #ffffff;
    --matcha-deep: #1a9547;
    --matcha-fresh: #62ad38;
    --brand-leaf: #5db64a;
    --ink: #231f20;
    --field-light: #c9e6b4;
    --field-mid: #6fbf4c;
  }
  html, body {
    margin: 0;
    padding: 0;
    width: 1200px;
    height: 1146px;
    overflow: hidden;
    background: var(--backdrop);
  }
  .canvas {
    position: relative;
    width: 1200px;
    height: 1146px;
  }
  .label {
    position: absolute;
    left: 197px;
    top: 48px;
    width: 806px;
    height: 1049px;
    display: block;
  }
  .label-sheet { fill: var(--label); }
  .brand-name {
    font-family: "Quicksand", sans-serif;
    font-weight: 400;
    font-size: 70px;
    fill: var(--brand-leaf);
  }
  .headline {
    font-family: "Oswald", sans-serif;
    font-weight: 600;
  }
  .headline-matcha { font-size: 136px; fill: var(--matcha-deep); }
  .headline-green-tea { font-size: 101px; fill: var(--matcha-fresh); }
  .descriptor {
    font-family: "Oswald", sans-serif;
    font-weight: 500;
    fill: var(--ink);
  }
  .descriptor-large { font-size: 57px; }
  .grade {
    font-family: "Oswald", sans-serif;
    font-weight: 600;
    font-size: 71px;
    fill: var(--matcha-deep);
  }
  .usage {
    font-family: "Oswald", sans-serif;
    font-weight: 500;
    font-size: 49px;
    fill: var(--ink);
  }
  .cert-badge {
    fill: none;
    stroke: var(--matcha-deep);
    stroke-width: 8;
  }
  .weight-pill { fill: var(--ink); }
  .weight-text {
    font-family: "Oswald", sans-serif;
    font-weight: 500;
    font-size: 19px;
    fill: #ffffff;
  }
</style>
</head>
<body>
<div class="canvas">
  <svg class="label" viewBox="440 315 620 807" xmlns="http://www.w3.org/2000/svg">
    <defs>
      <linearGradient id="fieldTone" x1="0" y1="0" x2="0" y2="1">
        <stop offset="0" stop-color="var(--field-light)"/>
        <stop offset="1" stop-color="var(--field-mid)"/>
      </linearGradient>
    </defs>

    <rect class="label-sheet" x="440" y="315" width="620" height="807"/>

    <text class="brand-name" x="570" y="455" textLength="318" lengthAdjust="spacingAndGlyphs">Leaf Hollow</text>

    <text class="headline headline-matcha" x="556" y="602" textLength="366" lengthAdjust="spacingAndGlyphs">MATCHA</text>
    <text class="headline headline-green-tea" x="556" y="698" textLength="372" lengthAdjust="spacingAndGlyphs">GREEN TEA</text>

    <ellipse class="cert-badge" cx="644" cy="768" rx="84" ry="42"/>

    <text class="descriptor descriptor-large" x="767" y="760" textLength="155" lengthAdjust="spacingAndGlyphs">Organic</text>
    <text class="descriptor descriptor-large" x="737" y="822" textLength="185" lengthAdjust="spacingAndGlyphs">Japanese</text>

    <text class="grade" x="558" y="898" textLength="370" lengthAdjust="spacingAndGlyphs">Premium Grade</text>

    <text class="usage" x="558" y="950" textLength="370" lengthAdjust="spacingAndGlyphs">PERFECT FOR DRINKING</text>
    <text class="usage" x="558" y="997" textLength="370" lengthAdjust="spacingAndGlyphs">BLENDING AND BAKING</text>

    <rect x="556" y="1010" width="372" height="80" fill="url(#fieldTone)" role="img" aria-label="Illustration of green mountains above rows of tea fields"/>

    <rect class="weight-pill" x="821" y="1061" width="64" height="23" rx="11.5"/>
    <text class="weight-text" x="853" y="1079" text-anchor="middle">100g</text>
  </svg>
</div>
</body>
</html>
```